Web Design For Metal Recycling Company

We are a scrap and recycling company dealing mainly in scrap metal base in Singapore. We deal in both domestic market and international market. Currently we are still unsure if we want to have a "lively" or "professional" company image so we will leave it to the designer to deem what is good.

We wish for a website to be able to "Retain" the interest of new visitor and at the same time able to give enough information for new and existing customer. We would also wish for design that will get the visitor to "Engage" us.

The attached is the logo for the company and we would want to incorporate that into the website. Either of the logo is fine.

```html
<!DOCTYPE html>
<html lang="en">
<head>
<meta charset="utf-8">
<title>Kim Hock Recycling</title>
<link href="https://fonts.googleapis.com/css2?family=Lato:wght@400;700;900&family=Orbitron:wght@500&display=swap" rel="stylesheet">
<style>
:root{
  --gold:#d4960a;
  --gold-dark:#b57f05;
  --gold-light:#e9b640;
  --grey:#7b7b7b;
  --white:#ffffff;
  --footer:#2b2b2b;
  --footer-deep:#212121;
  --footer-text:#a9a9a9;
}
*{margin:0;padding:0;box-sizing:border-box}
html,body{width:1200px;height:719px;overflow:hidden;background:var(--white)}
body{position:relative;font-family:"Lato",Arial,sans-serif}
.top-band{position:absolute;left:0;top:0;width:1200px;height:21px;background:var(--gold);border-bottom:1px solid var(--gold-dark)}
.site-header{position:absolute;left:0;top:21px;width:1200px;height:91px;background:var(--white);box-shadow:0 2px 3px rgba(0,0,0,.15);z-index:2}
.brand{position:absolute;left:172px;top:21px;display:flex;align-items:center;gap:10px}
.brand-square{width:44px;height:44px;border:3px solid var(--gold)}
.brand-name{font-weight:900;font-size:27px;color:var(--gold);letter-spacing:1px;text-transform:uppercase}
.support{position:absolute;right:171px;top:20px;display:flex;gap:6px;align-items:flex-start}
.support-label{font-family:"Orbitron",sans-serif;font-size:8.5px;color:var(--gold);text-transform:uppercase}
.support-phone{font-family:"Orbitron",sans-serif;font-size:14px;color:var(--grey);margin-top:1px;text-align:right}
.main-nav{position:absolute;right:171px;top:63px;display:flex;gap:26px;font-size:11px;font-weight:700;color:var(--grey);text-transform:uppercase}
.main-nav .active{color:var(--gold)}
.main-nav .about{margin-right:8px}
.hero{position:absolute;left:0;top:112px;width:1200px;height:367px;background:linear-gradient(to bottom,var(--gold) 0%,#e3b653 45%,#f6ead0 80%,#ffffff 100%)}
.tile{position:absolute}
.tile-furnace{left:177px;top:23px;width:428px;height:173px;background:linear-gradient(120deg,#7a4a12 0%,#c7821f 45%,#f0c060 60%,#9d6415 100%)}
.tile-wire{left:177px;top:198px;width:210px;height:146px;background:linear-gradient(135deg,#5a3018,#a7663c 50%,#4b2a16)}
.tile-sheet{left:388px;top:198px;width:217px;height:146px;background:linear-gradient(135deg,#6e685f,#b3a894 50%,#5c564e)}
.tile-cable{left:608px;top:23px;width:206px;height:321px;background:linear-gradient(160deg,#3a3f42,#59605f 45%,#2b2f31)}
.tile-board{left:818px;top:23px;width:205px;height:321px;background:linear-gradient(160deg,#4b5e4c,#778a72 50%,#3b4b3c)}
.hero-copy{position:absolute;left:204px;top:49px;width:360px;color:var(--white);font-size:14.5px;font-weight:700;line-height:17.5px;text-shadow:0 1px 2px rgba(0,0,0,.6)}
.hero-copy strong{font-weight:900;font-size:17px}
.cta{position:absolute;top:139px;height:28px;border:1px solid var(--white);background:rgba(212,150,10,.9);color:var(--white);font-size:10.5px;font-weight:900;text-transform:uppercase;padding:7px 0 0 13px}
.cta svg{position:absolute;right:10px;top:7px}
.cta-contact{left:202px;width:176px}
.cta-about{left:381px;width:176px}
.site-footer{position:absolute;left:0;top:479px;width:1200px;height:194px;background:var(--footer)}
.footer-title{position:absolute;top:33px;font-size:16px;font-weight:700;color:var(--gold)}
.address-list{position:absolute;left:179px;top:66px;list-style:none;font-family:Arial,sans-serif;font-size:10.5px;color:var(--footer-text);line-height:12px}
.address-list li{display:flex;gap:7px;margin-bottom:4px}
.address-list svg{flex:none;margin-top:1px}
.map{position:absolute;left:452px;top:64px;width:256px;height:105px;border:2px solid #bdbdbd;background:linear-gradient(135deg,#ebe8e2,#dedad2)}
.social{position:absolute;left:744px;top:64px;display:flex;gap:12px}
.social span{width:35px;height:35px;border-radius:50%;background:radial-gradient(circle at 40% 35%,#555,#2a2a2a);box-shadow:0 1px 2px #000}
.social span:first-child{background:radial-gradient(circle at 40% 35%,#4e6aa8,#223766)}
.copyright{position:absolute;left:0;top:673px;width:1200px;height:46px;background:var(--footer-deep);font-family:Arial,sans-serif;font-size:11.5px;color:var(--footer-text);text-align:center;padding-top:19px}
</style>
</head>
<body>
<div class="top-band"></div>
<header class="site-header">
  <div class="brand"><span class="brand-square"></span><span class="brand-name">Kim Hock Recycling</span></div>
  <div class="support">
    <svg width="22" height="24" viewBox="0 0 22 24"><circle cx="11" cy="8" r="6" fill="#d4960a"/><path d="M1 24c0-7 4-9 10-9s10 2 10 9z" fill="#d4960a"/></svg>
    <div><div class="support-label">Customer support:</div><div class="support-phone">+ 0099 88 77 66 55</div></div>
  </div>
  <nav class="main-nav"><span class="active">Home</span><span class="about">About us</span><span>Product &amp; Services</span><span>Contact us</span></nav>
</header>
<section class="hero">
  <div class="tile tile-furnace" role="img" aria-label="Molten metal being poured in a foundry"></div>
  <div class="tile tile-wire" role="img" aria-label="Pile of scrap copper wire"></div>
  <div class="tile tile-sheet" role="img" aria-label="Stack of scrap aluminium sheet"></div>
  <div class="tile tile-cable" role="img" aria-label="Cut ends of copper cables"></div>
  <div class="tile tile-board" role="img" aria-label="Scrap computer circuit boards"></div>
  <p class="hero-copy"><strong>Kim Hock,</strong> your One Stop Solution to all your scrap ferrous, Non-Ferrous and other recyclable. With more than <strong>30 years of experience</strong> in the industry, we know your needs.</p>
  <div class="cta cta-contact">Contact us now !
    <svg width="16" height="13" viewBox="0 0 16 13"><path d="M1 4c0-3 14-3 14 0v2h-4V4H5v2H1z M3 7h10l1 5H2z" fill="#fff"/></svg></div>
  <div class="cta cta-about">About us
    <svg width="14" height="14" viewBox="0 0 14 14"><circle cx="7" cy="7" r="7" fill="#fff"/><rect x="6" y="6" width="2" height="5" fill="#d4960a"/><circle cx="7" cy="4" r="1.1" fill="#d4960a"/></svg></div>
</section>
<footer class="site-footer">
  <h3 class="footer-title" style="left:178px">Address:</h3>
  <ul class="address-list">
    <li><svg width="12" height="10" viewBox="0 0 12 10"><path d="M6 0l6 5h-2v5H2V5H0z" fill="#d4960a"/></svg><span>18 Kranji Loop Industrial Park<br>Block 4<br>Singapore 730118</span></li>
    <li><svg width="12" height="10" viewBox="0 0 12 10"><path d="M0 3c0-3 12-3 12 0v1H9V3H3v1H0z M2 5h8l1 5H1z" fill="#d4960a"/></svg><span>(+65) 9120 4471</span></li>
    <li><svg width="12" height="10" viewBox="0 0 12 10"><rect x="0" y="3" width="12" height="7" fill="#d4960a"/><rect x="2" y="0" width="8" height="3" fill="#d4960a"/></svg><span>(+65) 63318809</span></li>
    <li><svg width="12" height="10" viewBox="0 0 12 10"><rect x="0.5" y="1.5" width="11" height="8" fill="none" stroke="#d4960a"/><path d="M1 2l5 4 5-4" fill="none" stroke="#d4960a"/></svg><span>hello@kimhockmetals.sg</span></li>
  </ul>
  <h3 class="footer-title" style="left:453px">Map:</h3>
  <div class="map" role="img" aria-label="Street map showing the yard location"></div>
  <h3 class="footer-title" style="left:746px">Social Media:</h3>
  <div class="social"><span></span><span></span><span></span></div>
</footer>
<div class="copyright">© Copyright 2014 Kim Hock Metals. All rights reserved.</div>
</body>
</html>
```